Kestin Executive Action Post card

I am an immigration attorney. President KESTIN is about to announce an immigration benefit in the next sixty days. I want a Postcard with Kestin photo speaking (bubble thought or something like that) that in spanish says something like. Hey, i already gave the order....and in the inside it would follow with "Now call Ramiro Quesada. the inside might have my logo, my address and my telepone and some sort of slogan.

Target Market(s)

Hispanic clientele, not very sophistacated.

Industry/Entity Type

Attorney

Font styles to use
Sans Serif

Colors

Designer to choose colors to be used in the design.

Requirements
Must have
• KESTIN
Spanish text
My logo
Easy to read telephone and address
Ramiro T. Quesada-Abogado de Inmigracion
20 Anos de Experiencia
17 Harlow Street Waltham MA 02187
781-555-0193
Nice to have
• Im looking for funny, and entertaining....not serious and elegant

```html
<!DOCTYPE html>
<html lang="es">
<head>
<meta charset="utf-8">
<title>Kestin Acción Ejecutiva – Postal</title>
<link rel="stylesheet" href="https://fonts.googleapis.com/css2?family=Oswald:wght@600&family=Comic+Neue:wght@400;700&family=Roboto:ital,wght@0,400;0,700;1,700&display=swap">
<style>
  :root {
    --backdrop: #e9e4dc;
    --front-black: #050505;
    --headline-yellow: #fff200;
    --white: #ffffff;
    --ink: #1a1a1a;
    --alert-red: #e3111b;
    --navy: #1e3170;
    --tan: #c6b78a;
    --rule-grey: #9a9a9a;
    --photo-dark: #2a1d18;
    --photo-mid: #5a3d2e;
  }
  * { box-sizing: border-box; margin: 0; padding: 0; }
  html, body { width: 1200px; height: 500px; overflow: hidden; }
  body { background: var(--backdrop); position: relative; font-family: "Roboto", Arial, sans-serif; }

  /* Front of postcard */
  .card-front {
    position: absolute; left: 25px; top: 33px; width: 560px; height: 435px;
    background: var(--front-black); overflow: hidden;
  }
  .speaker-photo {
    position: absolute; left: 0; top: 0; width: 215px; height: 435px;
    background: radial-gradient(ellipse at 55% 30%, var(--photo-mid) 0%, var(--photo-dark) 45%, var(--front-black) 80%);
  }
  .headline {
    position: absolute; left: 222px; top: 30px; width: 330px; text-align: center;
    font-family: "Oswald", Impact, sans-serif; font-weight: 600;
    color: var(--headline-yellow); font-size: 27px; line-height: 1.2;
  }
  .subheadline {
    position: absolute; left: 222px; top: 66px; width: 330px; text-align: center;
    font-family: "Roboto", Arial, sans-serif; font-weight: 700;
    color: var(--white); font-size: 15.5px;
  }
  .speech-bubble { position: absolute; left: 195px; top: 95px; width: 345px; height: 282px; }
  .bubble-text {
    position: absolute; left: 272px; top: 108px; width: 262px;
    font-family: "Comic Neue", "Comic Sans MS", sans-serif; color: var(--ink);
    font-size: 15.3px; line-height: 1.3;
  }
  .bubble-text .opener { font-weight: 700; font-size: 19px; display: block; margin-bottom: 2px; letter-spacing: 0.3px; }
  .bubble-text .phone { color: var(--alert-red); font-weight: 700; }
  .bubble-text strong { font-weight: 700; }
  .bubble-logo {
    position: absolute; left: 322px; top: 318px; display: flex; align-items: center; gap: 6px;
    font-family: "Roboto", Arial, sans-serif; font-weight: 400; font-size: 9px; color: var(--navy);
    text-transform: uppercase; line-height: 1.2;
  }
  .logo-square { width: 12px; height: 12px; background: var(--navy); flex: none; }

  /* Back of postcard */
  .card-back {
    position: absolute; left: 612px; top: 33px; width: 558px; height: 435px;
    background: var(--white); overflow: hidden;
  }
  .documents-photo {
    position: absolute; left: 0; top: 0; width: 270px; height: 180px;
    background: linear-gradient(135deg, #1d3a7a 0%, #c23b3b 45%, #e9eef2 70%, #c7d8c9 100%);
  }
  .attorney-panel {
    position: absolute; left: 0; top: 180px; width: 270px; height: 177px;
    background: var(--tan); text-align: center; padding-top: 20px;
  }
  .attorney-name {
    font-weight: 700; color: var(--navy); font-size: 19px; font-variant: small-caps; letter-spacing: 0.3px;
  }
  .attorney-title { font-weight: 700; font-style: italic; color: var(--ink); font-size: 14px; margin-top: 2px; }
  .attorney-years { font-weight: 700; color: var(--alert-red); font-size: 15px; margin-top: 7px; }
  .attorney-address { color: var(--ink); font-size: 14px; line-height: 1.3; margin-top: 8px; }
  .attorney-phone { font-weight: 700; color: var(--alert-red); font-size: 26px; margin-top: 4px; }

  .return-address { position: absolute; left: 275px; top: 30px; width: 150px; color: var(--ink); }
  .return-logo {
    display: flex; align-items: center; gap: 5px;
    font-size: 9px; font-weight: 400; color: var(--navy); text-transform: uppercase; line-height: 1.15;
  }
  .return-lines { text-align: center; font-size: 12px; line-height: 1.25; margin-top: 10px; width: 110px; }
  .stamp-box {
    position: absolute; left: 419px; top: 30px; width: 122px; height: 121px;
    border: 1px solid var(--rule-grey);
  }
  .mailing-lines { position: absolute; left: 300px; top: 232px; width: 241px; }
  .mailing-lines span { display: block; height: 1px; background: var(--rule-grey); margin-bottom: 34px; }
</style>
</head>
<body>
  <section class="card-front">
    <div class="speaker-photo" role="img" aria-label="Fotografía de Kestin hablando, con traje oscuro y corbata roja"></div>
    <h1 class="headline">Kestin Acción Ejecutiva</h1>
    <p class="subheadline">Beneficio de Inmigracíon</p>
    <svg class="speech-bubble" viewBox="0 0 345 282" aria-hidden="true">
      <path d="M72 2 H328 Q343 2 343 17 V265 Q343 280 328 280 H72 Q57 280 57 265 V245 L2 240 L57 205 V17 Q57 2 72 2 Z"
            fill="#ffffff" stroke="#9a9a9a" stroke-width="2"/>
    </svg>
    <p class="bubble-text">
      <span class="opener">Hey , yo ya di la orden . . .</span>
      Ahora llame Ramiro Quesada en este numero, <span class="phone">781.555.0193</span> o visitarlo en su oficina en 17 Harlow Street,Waltham, MA 02187. <strong>Ramiro T. Quesada</strong> es un abogado de inmigracíon con veinte años de experiencia.
    </p>
    <div class="bubble-logo"><span class="logo-square"></span><span>Law Office of<br>Ramiro T. Quesada</span></div>
  </section>

  <section class="card-back">
    <div class="documents-photo" role="img" aria-label="Fotografía de tarjetas de residencia y seguro social sobre una bandera"></div>
    <div class="attorney-panel">
      <p class="attorney-name">Ramiro T. Quesada</p>
      <p class="attorney-title">Abogado de Inmigracíon</p>
      <p class="attorney-years">20 Años de Experiencia</p>
      <p class="attorney-address">17 Harlow Street.<br>Waltham MA 02187</p>
      <p class="attorney-phone">781.555.0193</p>
    </div>
    <div class="return-address">
      <div class="return-logo"><span class="logo-square"></span><span>The Law Office of<br>Ramiro Quesada</span></div>
      <p class="return-lines">17 Harlow Street,<br>Waltham,<br>MA 02187.</p>
    </div>
    <div class="stamp-box"></div>
    <div class="mailing-lines"><span></span><span></span><span></span><span></span></div>
  </section>
</body>
</html>
```